Business Card Design Project

Oil & gas fabrication and Paint company. Need double sided with color. want original look. see attached but don't make similar!

Think Steel!

Business

```html
<!DOCTYPE html>
<html lang="en">
<head>
<meta charset="utf-8">
<title>Kestrel Business Card</title>
<link href="https://fonts.googleapis.com/css2?family=Merriweather:wght@400&family=Open+Sans:wght@400;600;800&display=swap" rel="stylesheet">
<style>
  :root {
    --navy: #1f2d8f;
    --navy-deep: #16207a;
    --steel: #8d8d8d;
    --steel-light: #c9c9c9;
    --orange: #f7a81b;
    --orange-light: #fdbf3a;
    --white: #ffffff;
    --backdrop: #e6e6e6;
    --ink: #1a1a1a;
  }
  * { margin: 0; padding: 0; box-sizing: border-box; }
  html, body { width: 1200px; height: 439px; overflow: hidden; }
  body {
    background: var(--backdrop);
    font-family: "Open Sans", Arial, sans-serif;
    position: relative;
  }
  .card {
    position: absolute;
    top: 70px;
    width: 530px;
    height: 300px;
    border-radius: 22px;
    overflow: hidden;
    box-shadow: 0 6px 18px rgba(0,0,0,0.18);
  }
  .card-front { left: 45px; background: var(--white); }
  .card-back {
    left: 625px;
    background: radial-gradient(ellipse at 50% 40%, var(--orange-light), var(--orange) 70%);
  }
  .front-waves { position: absolute; inset: 0; }
  .brand-name {
    position: absolute;
    font-family: "Open Sans", Arial, sans-serif;
    font-weight: 800;
    color: var(--navy);
    letter-spacing: 1px;
  }
  .front-brand { left: 34px; top: 52px; font-size: 38px; }
  .brand-dot {
    position: absolute;
    border-radius: 50%;
    background: var(--orange);
  }
  .front-dot { left: 214px; top: 66px; width: 18px; height: 18px; }
  .hotline {
    position: absolute;
    right: 34px;
    top: 20px;
    display: flex;
    align-items: center;
    gap: 6px;
    color: var(--orange);
    font-weight: 600;
    font-size: 18px;
  }
  .person-name {
    position: absolute;
    left: 52px;
    top: 150px;
    font-family: "Merriweather", Georgia, serif;
    font-size: 24px;
    color: var(--navy);
  }
  .contact-list {
    position: absolute;
    right: 38px;
    top: 110px;
    list-style: none;
    color: var(--white);
    font-size: 13.5px;
    line-height: 21.5px;
    text-align: right;
  }
  .contact-list li { display: flex; align-items: center; justify-content: flex-end; gap: 6px; }
  .contact-list li.gap-above { margin-top: 8px; }
  .contact-list svg { width: 12px; height: 12px; }
  .address {
    position: absolute;
    right: 30px;
    bottom: 20px;
    color: var(--white);
    font-size: 13.5px;
  }
  .back-brand-row {
    position: absolute;
    left: 0; right: 0;
    top: 100px;
    display: flex;
    justify-content: center;
    align-items: center;
    gap: 14px;
  }
  .back-brand-row .brand-name { position: static; font-size: 64px; }
  .back-brand-row .brand-dot { position: static; width: 30px; height: 30px; background: var(--navy); }
  .back-url {
    position: absolute;
    left: 0; right: 0;
    top: 220px;
    text-align: center;
    font-size: 18px;
    color: var(--ink);
  }
</style>
</head>
<body>

<section class="card card-front" aria-label="Business card front">
  <svg class="front-waves" viewBox="0 0 530 300" preserveAspectRatio="none" aria-hidden="true">
    <defs>
      <linearGradient id="steelBand" x1="0" y1="0" x2="1" y2="0">
        <stop offset="0" stop-color="#6e6e6e"/>
        <stop offset="0.5" stop-color="#d4d4d4"/>
        <stop offset="1" stop-color="#7a7a7a"/>
      </linearGradient>
      <linearGradient id="navyField" x1="0" y1="0" x2="0" y2="1">
        <stop offset="0" stop-color="#2836a3"/>
        <stop offset="1" stop-color="#16207a"/>
      </linearGradient>
    </defs>
    <path d="M0,246 C120,276 215,218 295,150 C365,90 440,72 530,78 L530,92 C440,88 368,104 300,162 C220,232 120,290 0,262 Z" fill="url(#steelBand)"/>
    <path d="M0,272 C120,300 222,242 302,172 C372,112 442,98 530,102 L530,300 L0,300 Z" fill="url(#navyField)"/>
  </svg>

  <div class="brand-name front-brand">KESTREL</div>
  <div class="brand-dot front-dot"></div>

  <div class="hotline">
    <svg width="20" height="20" viewBox="0 0 20 20" aria-hidden="true">
      <circle cx="10" cy="10" r="9" fill="none" stroke="currentColor" stroke-width="2"/>
      <path d="M7 5 L9 5 L9.6 8 L8.4 9 C9 10.4 9.8 11.2 11 11.8 L12 10.6 L15 11.2 L15 13 C11 14 6 9 7 5 Z" fill="currentColor"/>
    </svg>
    <span>1-800-555-WELD</span>
  </div>

  <div class="person-name">Dana Mercer</div>

  <ul class="contact-list">
    <li>
      <svg viewBox="0 0 12 12" aria-hidden="true"><circle cx="6" cy="6" r="5.3" fill="none" stroke="#fff" stroke-width="1.2"/><path d="M4 3 L5 3 L5.4 4.8 L4.8 5.4 C5.2 6.2 5.8 6.8 6.6 7.2 L7.2 6.6 L9 7 L9 8 C6.6 8.6 3.4 5.4 4 3 Z" fill="#fff"/></svg>
      <span>555-014-2290</span>
    </li>
    <li>
      <svg viewBox="0 0 12 12" aria-hidden="true"><rect x="3" y="0.5" width="6" height="11" rx="1" fill="none" stroke="#fff" stroke-width="1.2"/><circle cx="6" cy="9.5" r="0.8" fill="#fff"/></svg>
      <span>555-017-4438</span>
    </li>
    <li>
      <svg viewBox="0 0 12 12" aria-hidden="true"><rect x="1" y="4" width="10" height="6" rx="1" fill="#fff"/><rect x="3" y="1" width="6" height="3" fill="none" stroke="#fff" stroke-width="1"/></svg>
      <span>1-800-555-0163</span>
    </li>
    <li class="gap-above">
      <svg viewBox="0 0 12 12" aria-hidden="true"><rect x="0.8" y="2.5" width="10.4" height="7" fill="none" stroke="#fff" stroke-width="1.2"/><path d="M1 3 L6 7 L11 3" fill="none" stroke="#fff" stroke-width="1.2"/></svg>
      <span>dana@kestrelfab.net</span>
    </li>
    <li>
      <svg viewBox="0 0 12 12" aria-hidden="true"><circle cx="6" cy="6" r="5.2" fill="none" stroke="#fff" stroke-width="1.1"/><ellipse cx="6" cy="6" rx="2.2" ry="5.2" fill="none" stroke="#fff" stroke-width="1"/><path d="M1 6 H11" stroke="#fff" stroke-width="1"/></svg>
      <span>www.kestrelfab.net</span>
    </li>
  </ul>

  <div class="address">4820 County Road 12, Alder, TX 75000</div>
</section>

<section class="card card-back" aria-label="Business card back">
  <div class="back-brand-row">
    <div class="brand-name">KESTREL</div>
    <div class="brand-dot"></div>
  </div>
  <div class="back-url">www.kestrelfab.net</div>
</section>

</body>
</html>
```